Email Template for AI Website Builder Marketing Campaign

Update: All the designs submitted have too much content for an email template. I have attached a mockup example of a simplified design. Please follow this guideline to revise your design to be less "wordy" and have less content to optimize the delivery rate of the emails. I have also attached the images I used to create the mockup. Feel free to use these images for your revised designs.
Original Brief:
I need a catchy email template for my new AI Website Builder, FolioNova.ai. The template must be professional, colorful, yet not too complex. The concept of the product is this:
FolioNova uses Artificial Intelligence (AI) to instantly build stunning websites, absolutely FREE. The user simply specifies their business name and business category (industry), and their stunning new website appears before their eyes!
The template will be used in MailChimp, so please provide the code that I can simply paste into the email body.
Here is a screenshot of our new website (which is not online yet) so you can match the color scheme and style of the email template to the new website design:
https://brindlemesh.com/mock_img/7720518/2638140/58190374/q8rt2lbw4k7ehnpyd3umc0xsvo_image.jpg
Let me know if you have any questions.
Thanks!
All submitted designs are too lengthy (too much content) for an email template. I will provide a mockup showing a sample of how you can simplify your design to function better as an email template and better suit my needs. I appreciate your patience!

```html
<!DOCTYPE html>
<html lang="en">
<head>
<meta charset="utf-8">
<title>FolioNova – Free AI Website Email</title>
<link href="https://fonts.googleapis.com/css2?family=Roboto:wght@400;500;700&display=swap" rel="stylesheet">
<style>
  :root {
    --navy: #0a1526;
    --navy-deep: #071020;
    --footer-navy: #0c1d33;
    --blue: #1591ef;
    --blue-bright: #1aa3f5;
    --cyan: #3dd1ea;
    --ice: #e8f3fc;
    --ink: #2a2a2a;
    --white: #ffffff;
  }
  * { box-sizing: border-box; margin: 0; padding: 0; }
  html, body { width: 1200px; height: 2320px; overflow: hidden; background: var(--white); }
  body { font-family: "Roboto", Arial, sans-serif; position: relative; }

  .backdrop { position: absolute; inset: 0; width: 1200px; height: 2320px; }

  .brand { position: absolute; display: flex; align-items: center; color: var(--white); font-weight: 700; }
  .brand-mark { background: linear-gradient(135deg, var(--cyan), var(--blue)); border-radius: 8px; }
  .brand--top { left: 112px; top: 84px; font-size: 40px; gap: 16px; }
  .brand--top .brand-mark { width: 48px; height: 48px; }
  .brand--foot { left: 112px; top: 2136px; font-size: 62px; gap: 20px; }
  .brand--foot .brand-mark { width: 70px; height: 70px; }

  .phone-pill {
    position: absolute; left: 805px; top: 78px; width: 280px; height: 66px;
    border-radius: 33px; background: linear-gradient(180deg, var(--blue-bright), var(--blue));
    display: flex; align-items: center; gap: 22px; padding-left: 14px;
    color: var(--white); font-weight: 700; font-size: 23px;
  }
  .phone-pill .icon { width: 40px; height: 40px; border-radius: 50%; background: var(--white); display: flex; align-items: center; justify-content: center; }

  .hero-title {
    position: absolute; left: 0; top: 280px; width: 1200px; text-align: center;
    color: var(--white); font-weight: 700; font-size: 62px; line-height: 84px;
  }
  .hero-title .accent { color: var(--cyan); }
  .hero-title .accent-blue { color: var(--blue-bright); font-size: 64px; }

  .btn {
    position: absolute; display: flex; align-items: center; justify-content: center;
    border-radius: 36px; color: var(--white); font-weight: 700; font-size: 26px;
    background: linear-gradient(180deg, var(--blue-bright), #0c7fe0);
  }
  .btn--hero { left: 424px; top: 574px; width: 354px; height: 66px; }
  .btn--dark { left: 408px; top: 1904px; width: 384px; height: 68px; background: var(--navy); }
  .btn--foot { left: 724px; top: 2139px; width: 383px; height: 67px; font-size: 27px; }

  .pitch {
    position: absolute; left: 108px; top: 1040px; width: 500px;
    font-weight: 700; font-size: 45px; line-height: 70px; color: var(--ink);
  }
  .pitch .accent { color: var(--blue-bright); }

  .illustration {
    position: absolute; left: 615px; top: 955px; width: 550px; height: 530px;
    border-radius: 40px;
    background: radial-gradient(circle at 45% 40%, #0f2440 0 22%, #cfe5f7 23% 60%, #eef6fd 61%);
  }

  .info-card {
    position: absolute; left: 112px; top: 1590px; width: 976px; height: 460px;
    border-radius: 22px; background: linear-gradient(180deg, #0b7fe1, #34b9d3);
  }
  .info-card p {
    position: absolute; left: 60px; top: 70px; width: 856px; text-align: center;
    color: var(--white); font-size: 27px; line-height: 54px;
  }

  .address { position: absolute; left: 112px; top: 2240px; color: var(--white); font-size: 17px; }
  .unsubscribe { position: absolute; left: 984px; top: 2230px; color: var(--white); font-size: 19px; font-weight: 700; text-decoration: underline; }
  .code { position: absolute; left: 1144px; top: 2262px; color: var(--white); font-size: 15px; }
</style>
</head>
<body>
  <svg class="backdrop" viewBox="0 0 1200 2320" aria-hidden="true">
    <defs>
      <linearGradient id="headerFill" x1="0" y1="0" x2="0" y2="1">
        <stop offset="0" stop-color="#0b1729"/>
        <stop offset="1" stop-color="#050d1a"/>
      </linearGradient>
    </defs>
    <!-- header band with cyan stripe -->
    <polygon points="0,640 420,880 1200,700 1200,670 420,845 0,600" fill="#1ab8ec"/>
    <polygon points="0,0 1200,0 1200,680 420,860 0,615" fill="url(#headerFill)"/>
    <!-- faint left shapes -->
    <polygon points="0,690 70,680 180,800 110,820" fill="#e6f1fb"/>
    <polygon points="10,820 60,800 170,900 120,910" fill="#eef5fc"/>
    <!-- footer band -->
    <polygon points="0,1820 1200,1740 1200,1760 0,1850" fill="#1ab8ec"/>
    <polygon points="0,1840 1200,1755 1200,2320 0,2320" fill="#0c1d33"/>
  </svg>

  <div class="brand brand--top"><span class="brand-mark"></span>FolioNova</div>

  <div class="phone-pill">
    <span class="icon">
      <svg width="22" height="22" viewBox="0 0 24 24"><path fill="#1591ef" d="M6.6 10.8a15.1 15.1 0 0 0 6.6 6.6l2.2-2.2a1 1 0 0 1 1-.25 11.4 11.4 0 0 0 3.6.57 1 1 0 0 1 1 1V20a1 1 0 0 1-1 1A17 17 0 0 1 3 4a1 1 0 0 1 1-1h3.5a1 1 0 0 1 1 1c0 1.25.2 2.45.57 3.57a1 1 0 0 1-.25 1z"/></svg>
    </span>
    +1 555 010 0199
  </div>

  <h1 class="hero-title">
    Your <span class="accent">FREE</span> Stunning<br>
    Website In 1-Click Built By<br>
    <span class="accent-blue">Artificial Intelligence</span>
  </h1>

  <a class="btn btn--hero">Build My Free Website</a>

  <h2 class="pitch">
    Harness the Power of Artificial Intelligence to Instantly Build Your Amazing <span class="accent">FREE Website Today!</span>
  </h2>

  <div class="illustration" role="img" aria-label="Isometric illustration of a website page rising into a glowing brand badge"></div>

  <section class="info-card">
    <p>FolioNova is the World's first website builder that builds professional, high-quality websites in seconds! Say goodbye to the traditional expensive and time-conuming methods of getting your business online!</p>
  </section>
  <a class="btn btn--dark">Generate FREE Site Now</a>

  <div class="brand brand--foot"><span class="brand-mark"></span>FolioNova</div>
  <a class="btn btn--foot">Get Your FREE Website</a>
  <div class="address">FolioNova, 4820 Harbor Lane, Milford DE 19963</div>
  <a class="unsubscribe">Unsubscribe</a>
  <div class="code">C 58</div>
</body>
</html>
```